Invite Card (Ministers) (business cards used for personal invitation to our church)

I need a business card sized advertisement. The card is a replacement for the attached card only much much cooler. I do not want a image background but more of a vectored, flat look with advertising colors.

I have attached a new image of the couple to replace the old image and a new logo to replace the old logo.

I need a PSD with ALL of the layers un-merged & unlocked

The back of the card should carry the same information as the old card.

Use advertising color and a modern flat look and feel.

Target Market(s)

professional audience

Industry/Entity Type

Non-Profit

Contact Information for Business Card

The card is a replacement for the attached card only much much cooler. I do not want a image background but more of a vectored, flat look with advertising colors.

Font styles to use
Sans Serif

Requirements
Must have
• Must have new logo, new image of couple
Should not have
• graphical background

```html
<!DOCTYPE html>
<html lang="en">
<head>
<meta charset="utf-8">
<title>Invite Card – Front and Back</title>
<link rel="stylesheet" href="https://fonts.googleapis.com/css2?family=Josefin+Sans:wght@400;600&family=Open+Sans:wght@400;600&display=swap">
<style>
  :root {
    --page-bg: #e9e6e1;
    --sky-top: #4fbbe6;
    --sky-bottom: #9fd3ec;
    --portrait-light: #a7a2a8;
    --portrait-dark: #3b3d52;
    --accent-blue: #1fa8e0;
    --text-white: #ffffff;
    --card-shadow: rgba(40, 30, 20, 0.28);
  }
  * { box-sizing: border-box; margin: 0; padding: 0; }
  html, body { width: 1200px; height: 913px; overflow: hidden; }
  body {
    background: var(--page-bg);
    display: flex;
    align-items: center;
    justify-content: center;
    gap: 60px;
  }
  .card {
    position: relative;
    width: 520px;
    height: 297px;
    border-radius: 4px;
    overflow: hidden;
    box-shadow: 0 10px 28px var(--card-shadow);
    color: var(--text-white);
  }
  .card-backdrop {
    position: absolute; inset: 0;
    background: linear-gradient(180deg, var(--sky-top) 0%, var(--sky-bottom) 100%);
  }

  /* Front */
  .front-shapes { position: absolute; inset: 0; }
  .invite-heading {
    position: absolute;
    top: 42px; left: 300px;
    font-family: "Josefin Sans", sans-serif;
    font-weight: 600;
    font-size: 24px;
    line-height: 1.1;
    letter-spacing: 3px;
  }
  .brand-name {
    position: absolute;
    top: 112px; left: 298px;
    font-family: "Josefin Sans", sans-serif;
    font-weight: 600;
    font-size: 46px;
    line-height: 1;
    letter-spacing: 1px;
    color: var(--text-white);
  }
  .pastors {
    position: absolute;
    left: 22px; bottom: 12px;
    font-family: "Open Sans", sans-serif;
    font-weight: 400;
    font-size: 11px;
    letter-spacing: 1px;
  }

  /* Back */
  .back-info {
    position: absolute;
    top: 52px; left: 58px;
    width: 404px;
    font-family: "Open Sans", sans-serif;
    font-size: 14px;
    letter-spacing: 0.5px;
    text-transform: uppercase;
  }
  .contact-line { text-align: center; line-height: 1.45; }
  .schedule { margin-top: 26px; list-style: none; }
  .schedule-row {
    display: flex;
    align-items: baseline;
    line-height: 2;
  }
  .schedule-row .leader {
    flex: 1;
    border-bottom: 2px dotted var(--text-white);
    margin: 0 6px;
    transform: translateY(-4px);
  }
</style>
</head>
<body>

  <section class="card card-front" aria-label="Invitation card front">
    <div class="card-backdrop"></div>
    <svg class="front-shapes" width="520" height="297" viewBox="0 0 520 297">
      <defs>
        <linearGradient id="portrait-fill" x1="0" y1="0" x2="0.6" y2="1">
          <stop offset="0" stop-color="#a7a2a8"/>
          <stop offset="1" stop-color="#3b3d52"/>
        </linearGradient>
      </defs>
      <path role="img" aria-label="Portrait of the pastor couple"
            d="M0 0 H222 C292 70 276 195 186 258 H0 Z" fill="url(#portrait-fill)"/>
      <path d="M222 0 C292 70 276 195 186 258" fill="none" stroke="var(--accent-blue)" stroke-width="8"/>
    </svg>
    <h1 class="invite-heading">YOU'RE<br>INVITED</h1>
    <div class="brand-name">OPEN<br>DOOR</div>
    <p class="pastors">PASTOR DANIEL &amp; MIRIAM HALE</p>
  </section>

  <section class="card card-back" aria-label="Invitation card back">
    <div class="card-backdrop"></div>
    <div class="back-info">
      <p class="contact-line">P: 1-800-555-0142</p>
      <p class="contact-line">www.opendoorfellowship.org</p>
      <p class="contact-line">A: 2480 W. Cedar Lane - Brookfield, TX 75000</p>
      <ul class="schedule">
        <li class="schedule-row"><span>Sunday</span><span class="leader"></span><span>9:00 AM</span></li>
        <li class="schedule-row"><span>Sunday</span><span class="leader"></span><span>11: AM</span></li>
        <li class="schedule-row"><span>Wed. Bible Class</span><span class="leader"></span><span>7:00 PM</span></li>
      </ul>
    </div>
  </section>

</body>
</html>
```